QORLIN Business card. A.I. company developing trading strategies.

My name is marcello bianchi and I'm CEO and co-founder of QORLIN Research, an AI company focusing on generating Ai-driven trading strategies.
This is our website: https://qorlin-analytics.example/
Values of our company: tech & R&D driven (we're all very mathy/stats/data driven), sophisticated (we only look for sophisticated, high knowledge investors), reserved (we don't go around telling anyone what we do).
Our main product: PivotFund. A trading strategy that delivered 70% in 2022 and 20% in 2023 so far.
Our main potential clients: HNW individuals, hedge funds, asset managers, tech entrepreneur.
Target Market(s)
Hedge funds, asset managers, High Net Worth individuals, Pension funds
Contact Information for Business Card
The basic: name, job title, company name, address, mail, phone number

```html
<!DOCTYPE html>
<html lang="en">
<head>
<meta charset="UTF-8">
<title>QORLIN Research — Business Card</title>
<link href="https://fonts.googleapis.com/css2?family=Montserrat:wght@300;400;500;700&display=swap" rel="stylesheet">
<style>
  :root {
    --backdrop: #232323;
    --card-dark: #141414;
    --card-light: #ffffff;
    --brand-red: #b91f37;
    --ink: #1a1a1a;
    --ink-soft: #2c2c2c;
  }
  * { box-sizing: border-box; margin: 0; padding: 0; }
  html, body {
    width: 1200px; height: 900px; overflow: hidden;
    background: var(--backdrop);
    font-family: "Montserrat", Arial, sans-serif;
  }
  .stage {
    position: relative; width: 1200px; height: 900px;
    display: flex; flex-direction: column; align-items: center; justify-content: center; gap: 40px;
  }
  .card {
    position: relative; width: 660px; height: 377px;
    border-radius: 22px; overflow: hidden;
  }
  /* Back side */
  .card--back {
    background: var(--card-dark);
    display: flex; align-items: center; justify-content: center;
  }
  .wordmark { display: flex; align-items: center; gap: 12px; }
  .wordmark__name {
    font-weight: 300; font-size: 64px; letter-spacing: 10px; line-height: 1;
  }
  .wordmark__dot {
    width: 12px; height: 12px; border-radius: 50%; background: var(--brand-red);
  }
  .card--back .wordmark__name { color: var(--card-light); }

  /* Front side */
  .card--front { background: var(--card-light); }
  .card__swoosh { position: absolute; inset: 0; width: 100%; height: 100%; }
  .card__brand {
    position: absolute; left: 34px; top: 118px; width: 260px;
    display: flex; justify-content: center;
  }
  .card--front .wordmark__name { color: var(--ink); font-size: 46px; letter-spacing: 6px; }
  .card__divider {
    position: absolute; left: 318px; top: 80px; width: 1.5px; height: 190px;
    background: var(--brand-red);
  }
  .contact {
    position: absolute; left: 342px; top: 78px; right: 20px; color: var(--ink-soft);
  }
  .contact__name {
    font-weight: 700; font-size: 26px; color: var(--brand-red);
    text-transform: uppercase; letter-spacing: 0.3px; line-height: 1.05;
    white-space: nowrap;
  }
  .contact__role { font-size: 15px; font-weight: 400; margin-bottom: 14px; }
  .contact__address { font-size: 15px; line-height: 1.35; margin-bottom: 12px; }
  .contact__list { list-style: none; font-size: 15px; line-height: 1.55; }
  .contact__list li { display: flex; align-items: center; gap: 9px; white-space: nowrap; }
  .contact__icon { width: 13px; height: 13px; fill: var(--brand-red); flex: none; }
</style>
</head>
<body>
<main class="stage">
  <section class="card card--back" aria-label="Business card, back">
    <div class="wordmark">
      <span class="wordmark__name">QORLIN</span>
      <span class="wordmark__dot"></span>
    </div>
  </section>

  <section class="card card--front" aria-label="Business card, front">
    <svg class="card__swoosh" viewBox="0 0 660 377" preserveAspectRatio="none" aria-hidden="true">
      <path d="M0,232 C170,320 390,352 660,346 L660,377 L0,377 Z" fill="var(--brand-red)"/>
      <path d="M250,315 C400,340 530,338 660,326 L660,341 C530,349 400,346 250,315 Z" fill="var(--card-light)"/>
      <path d="M250,315 C400,338 530,334 660,322 L660,332 C530,342 400,342 250,315 Z" fill="var(--ink)"/>
    </svg>

    <div class="card__brand">
      <div class="wordmark">
        <span class="wordmark__name">QORLIN</span>
        <span class="wordmark__dot"></span>
      </div>
    </div>

    <div class="card__divider"></div>

    <div class="contact">
      <h1 class="contact__name">Marcello Bianchi</h1>
      <p class="contact__role">CEO and Co-Founder</p>
      <p class="contact__address">742 Harbor Lane<br>Lakeview City ZZ 4190</p>
      <ul class="contact__list">
        <li>
          <svg class="contact__icon" viewBox="0 0 24 24"><path d="M6.6 10.8a15.1 15.1 0 0 0 6.6 6.6l2.2-2.2c.3-.3.7-.4 1-.2 1.1.4 2.3.6 3.6.6.6 0 1 .4 1 1V20c0 .6-.4 1-1 1A17 17 0 0 1 3 4c0-.6.4-1 1-1h3.5c.6 0 1 .4 1 1 0 1.3.2 2.5.6 3.6.1.3 0 .7-.2 1z"/></svg>
          555-018-3364
        </li>
        <li>
          <svg class="contact__icon" viewBox="0 0 24 24"><path d="M2 5h20v14H2z M3.5 6.5 12 13l8.5-6.5" fill="var(--brand-red)" stroke="var(--card-light)" stroke-width="1.5"/></svg>
          info@qorlin-analytics.example
        </li>
        <li>
          <svg class="contact__icon" viewBox="0 0 24 24"><circle cx="12" cy="12" r="10"/><path d="M2 12h20M12 2c3 3 3 17 0 20M12 2c-3 3-3 17 0 20" fill="none" stroke="var(--card-light)" stroke-width="1.3"/></svg>
          www.qorlin-analytics.example
        </li>
      </ul>
    </div>
  </section>
</main>
</body>
</html>
```